brisk-vale.com Real Estate, Investment, Financial corporate

Real Estate, Investment, Financial corporate looking site. Show present a professional firm, with an elegant display. Please see the attached file which includes the logo, palette and fonts.
Updates

We just starting the brief today. ( logo was delayed)

Target Market(s)

Investors, Corporate , B2b

Industry/Entity Type

real-estate investments

Number of Pages Required

3 page

Requirements
Must have
• Dazzling Homepage
Nice to have
• paralex

```html
<!DOCTYPE html>
<html lang="en">
<head>
<meta charset="utf-8">
<title>Brisk Vale Real Estate</title>
<link href="https://fonts.googleapis.com/css2?family=Playfair+Display:wght@700&family=Raleway:wght@400;500;600&display=swap" rel="stylesheet">
<style>
:root{
  --gold:#e8b830;
  --gold-deep:#c9a22c;
  --gold-dark:#b8911f;
  --ink:#0b0b0b;
  --text:#222;
  --muted:#555;
  --light:#f0f0f0;
  --line:#d9d9d9;
  --white:#fff;
  --serif:'Playfair Display', Georgia, serif;
  --sans:'Raleway', Arial, sans-serif;
}
*{margin:0;padding:0;box-sizing:border-box}
html,body{width:1200px;height:5305px;overflow:hidden;background:var(--white);font-family:var(--sans);color:var(--text)}
.page{position:relative;width:1200px;height:5305px}
.abs{position:absolute}
.btn{position:absolute;background:var(--gold-deep);color:var(--white);font:600 14px var(--sans);letter-spacing:2px;display:flex;align-items:center;justify-content:center;text-transform:uppercase}

/* header */
.site-header{left:0;top:0;width:1200px;height:88px;background:var(--ink)}
.brand{display:flex;align-items:center;gap:14px}
.brand-mark{width:50px;height:50px;border:2px solid var(--gold)}
.brand-name{font:700 24px var(--serif);color:var(--white);line-height:1}
.brand-sub{font:500 12px var(--sans);color:var(--white);letter-spacing:4px;margin-top:4px}
.nav a{position:absolute;top:33px;color:var(--white);font:500 16px var(--sans);text-decoration:none}
.call-box{left:926px;top:0;width:274px;height:88px;background:var(--gold-deep);clip-path:polygon(28px 0,100% 0,100% 100%,0 100%)}
.call-box .lbl{position:absolute;left:94px;top:24px;font:500 14px var(--sans);color:var(--white)}
.call-box .num{position:absolute;left:94px;top:42px;font:600 19px var(--sans);color:var(--white);letter-spacing:1px}

/* hero */
.hero{left:0;top:88px;width:1200px;height:750px;overflow:hidden}
.hero-photo{position:absolute;inset:0;background:linear-gradient(100deg,#3d3a37 0%,#6a645c 45%,#8d8a86 70%,#b8bab4 100%)}
.hero-shade{position:absolute;inset:0;background:linear-gradient(90deg,rgba(0,0,0,.55),rgba(0,0,0,0) 60%)}
.hero-person{position:absolute;left:760px;top:60px;width:300px;height:690px;background:linear-gradient(180deg,#4a3a30 0%,#1f4d9a 30%,#183d80 100%);border-radius:120px 120px 0 0}
.hero-kicker{left:111px;top:421px;font:500 23px var(--sans);color:var(--white);letter-spacing:1.5px}
.hero-title{left:111px;top:452px;font:700 60px/66px var(--serif);color:var(--white)}

/* stats */
.stat{position:absolute;top:959px;width:308px;height:163px;background:var(--ink);color:var(--white)}
.stat .num{position:absolute;left:106px;top:36px;font:700 46px var(--serif)}
.stat .lab{position:absolute;left:110px;top:97px;font:500 17px var(--sans)}
.stat svg{position:absolute;left:18px;top:48px}

.quote{left:0;top:1205px;width:1200px;text-align:center;font:700 34px/48px var(--serif);color:#1a1a1a}

/* about */
.about-head{left:111px;top:1474px;width:470px;font:700 25px/34px var(--serif);color:#111}
.about-body{left:111px;top:1636px;width:430px;font:400 15px/24.5px var(--sans);color:#333}
.ph{position:absolute}

/* provide */
.provide{left:0;top:2171px;width:1200px;height:628px;background:linear-gradient(120deg,#c7a02a,#b48f22 50%,#c9a535)}
.section-title{position:absolute;left:0;width:1200px;text-align:center;font:700 44px var(--serif)}
.oct{position:absolute;top:2381px;width:308px;height:303px;clip-path:polygon(30% 0,70% 0,100% 30%,100% 70%,70% 100%,30% 100%,0 70%,0 30%);text-align:center}
.oct h3{font:700 21px var(--serif);margin-top:78px}
.oct p{font:400 15px/26px var(--sans);margin:8px 28px 0}
.oct-num{position:absolute;top:2350px;font:700 64px var(--serif);width:308px;text-align:center}

/* projects */
.proj-overlay{position:absolute;left:0;right:0;bottom:0;padding:0 28px 72px;color:var(--white)}

/* reasons */
.reasons{left:0;top:3740px;width:1200px;height:788px;background:linear-gradient(160deg,#5a5a5a,#3b3b3b 50%,#4d4d4d)}
.hex{position:absolute;top:3948px;width:286px;height:467px}
.hex svg.shape{position:absolute;inset:0}
.hex .in{position:absolute;left:0;top:210px;width:286px;text-align:center}
.hex h3{font:700 21px var(--serif);color:#111}
.hex p{font:400 15px/26px var(--sans);color:#333;margin:8px 24px 0}

/* map & footer */
.map{left:0;top:4528px;width:1200px;height:264px;background:linear-gradient(135deg,#e6e6e6,#d6d6d6 50%,#e2e2e2)}
.map-label{left:638px;top:4640px;width:176px;height:48px;background:var(--white);font:500 15px/18px var(--sans);color:var(--gold-deep);padding:6px 8px}
.foot-h{position:absolute;font:700 20px var(--serif);color:#111}
.foot-links a{display:block;font:400 15px var(--sans);color:#222;text-decoration:none;margin-bottom:17px}
.field{position:absolute;border:1px solid #bbb;font:400 14px var(--sans);color:#888;padding:12px 16px}
.social{position:absolute;top:5103px;width:44px;height:44px;border-radius:50%;background:var(--gold-deep)}
.copy{left:0;top:5232px;width:1200px;text-align:center;font:500 13px var(--sans);letter-spacing:1.5px;color:#333}
</style>
</head>
<body>
<div class="page">

  <header class="abs site-header">
    <div class="abs brand" style="left:111px;top:19px">
      <div class="brand-mark"></div>
      <div><div class="brand-name">Brisk Vale</div><div class="brand-sub">REAL ESTATE</div></div>
    </div>
    <nav class="nav">
      <a style="left:401px">Home</a>
      <a style="left:498px">About Us</a>
      <a style="left:620px">Projects</a>
      <a style="left:733px">Blog</a>
      <a style="left:817px">Contact</a>
    </nav>
    <div class="abs" style="left:427px;top:14px;width:2px;height:10px;background:#fff"></div>
    <div class="abs" style="left:427px;top:62px;width:2px;height:10px;background:#fff"></div>
    <div class="abs call-box">
      <svg class="abs" style="left:48px;top:26px" width="34" height="34" viewBox="0 0 24 24" fill="none" stroke="#fff" stroke-width="1.4"><path d="M5 3h4l2 5-3 2a12 12 0 0 0 6 6l2-3 5 2v4a2 2 0 0 1-2 2A18 18 0 0 1 3 5a2 2 0 0 1 2-2z"/></svg>
      <div class="lbl">Call Us:</div>
      <div class="num">555-318-2046</div>
    </div>
  </header>

  <section class="abs hero">
    <div class="hero-photo" role="img" aria-label="Photo of a brick family house at dusk"></div>
    <div class="hero-shade"></div>
    <svg class="abs" style="left:0;top:0" width="1200" height="750">
      <polygon points="700,750 1110,750 1200,600 1200,290 1090,290" fill="#c9a22c"/>
    </svg>
    <div class="hero-person" role="img" aria-label="Photo of a smiling businessman in a blue suit"></div>
  </section>
  <div class="abs hero-kicker">WE PROVIDE BEST FINANCIAL SOLUTIONS</div>
  <h1 class="abs hero-title">For Highest Quality<br>Real Estate</h1>
  <div class="btn" style="left:111px;top:626px;width:177px;height:47px">Contact Us</div>
  <svg class="abs" style="left:111px;top:758px" width="110" height="24" fill="none" stroke-width="2"><path d="M2 12h40M2 12l10-9M2 12l10 9" stroke="#fff"/><path d="M66 12h40M106 12l-10-9M106 12l-10 9" stroke="#e8b830"/></svg>

  <div class="stat" style="left:111px">
    <div class="abs" style="inset:0;background:linear-gradient(120deg,#2a2a2a,#0b0b0b 60%)" role="img" aria-label="Dark photo of banknotes"></div>
    <svg width="76" height="70" viewBox="0 0 76 70" fill="none" stroke="#e8b830" stroke-width="2.5"><rect x="6" y="30" width="30" height="36"/><rect x="36" y="14" width="26" height="52"/><path d="M12 40h8M12 50h8M44 26h8M44 38h8M44 50h8"/></svg>
    <div class="num">1850 <span style="font-weight:400">+</span></div><div class="lab">Investment Completed</div>
  </div>
  <div class="stat" style="left:447px">
    <svg width="76" height="70" viewBox="0 0 76 70" fill="none" stroke="#e8b830" stroke-width="2.5"><rect x="4" y="24" width="22" height="42"/><rect x="26" y="6" width="24" height="60"/><rect x="50" y="30" width="22" height="36"/><path d="M10 34h10M10 46h10M32 18h12M32 32h12M32 46h12M56 40h10"/></svg>
    <div class="num">1000 <span style="font-weight:400">+</span></div><div class="lab">Completed Project</div>
  </div>
  <div class="stat" style="left:780px">
    <svg width="76" height="70" viewBox="0 0 76 70" fill="none" stroke="#e8b830" stroke-width="2.5"><circle cx="38" cy="28" r="8"/><circle cx="18" cy="36" r="6"/><circle cx="58" cy="36" r="6"/><path d="M24 64c0-12 28-12 28 0M6 64c0-10 18-12 20-8M70 64c0-10-18-12-20-8M30 4l3 6 6 1-5 4 2 6-6-3-6 3 2-6-5-4 6-1z"/></svg>
    <div class="num">2000 <span style="font-weight:400">+</span></div><div class="lab">Happy Clients</div>
  </div>

  <p class="abs quote">“ We Are Business Organization Providing &nbsp;You<br>Particular Service On Your Business ”</p>

  <h2 class="abs about-head">Lorem ipsum dolor sit amet, consectetur adipiscing elit, sed do eiusmod tempor ci ut labore et dolore magna aliquauis ipsu msuspendisse.</h2>
  <p class="abs about-body">Lorem ipsum dolor sit amet, consectetur adipiscing is elit, sed do eiusmod tempor incididunt ut labore etos dolore magna aliqua. Ut enim ad minim veniam quisit nostrud exercitation ullamco laboris nisi ut aliquip ex ea commodo consequat reprehenderit.</p>
  <div class="btn" style="left:111px;top:1815px;width:177px;height:46px">Know More</div>
  <div class="ph" style="left:838px;top:1383px;width:249px;height:264px;background:var(--gold)"></div>
  <div class="ph" style="left:556px;top:1716px;width:154px;height:227px;background:var(--gold)"></div>
  <div class="ph" style="left:613px;top:1432px;width:393px;height:511px;background:linear-gradient(160deg,#f2f2f2 0%,#8a8f96 35%,#1f242a 70%,#111 100%)" role="img" aria-label="Photo of glass skyscrapers seen from below"></div>
  <div class="ph" style="left:743px;top:1647px;width:344px;height:405px;background:var(--white);box-shadow:0 4px 14px rgba(0,0,0,.15)"></div>
  <div class="ph" style="left:759px;top:1663px;width:311px;height:372px;background:linear-gradient(170deg,#d8dde0 0%,#b7c3c8 45%,#c9603a 75%,#2f3540 100%)" role="img" aria-label="Photo of two women working on a laptop in an office"></div>

  <section class="abs provide" role="img" aria-label="Gold-tinted photo of a businessman reviewing papers"></section>
  <h2 class="section-title" style="top:2276px;color:#fff">What We Provide</h2>
  <svg class="abs" style="left:36px;top:2519px" width="1130" height="24" fill="none" stroke="#fff" stroke-width="2"><path d="M2 12h40M2 12l10-9M2 12l10 9M1088 12h40M1128 12l-10-9M1128 12l-10 9"/></svg>

  <div class="oct" style="left:111px;background:var(--ink);color:#fff">
    <h3>Real Estate Development</h3>
    <p>Lorem ipsum dolor sit amet consectetur adipiscing elit, sed do eiusmod tempor incididunt ut labore et dolore</p>
    <svg style="margin-top:20px" width="34" height="20" fill="none" stroke="#e8b830" stroke-width="2"><path d="M2 10h30M32 10l-8-7M32 10l-8 7"/></svg>
  </div>
  <div class="oct-num" style="left:111px;color:#fff">1</div>
  <div class="oct" style="left:447px;background:var(--light);color:#222">
    <h3>Property Management</h3>
    <p>Lorem ipsum dolor sit amet consectetur adipiscing elit, sed do eiusmod tempor incididunt ut labore et dolore</p>
    <svg style="margin-top:20px" width="34" height="20" fill="none" stroke="#111" stroke-width="2"><path d="M2 10h30M32 10l-8-7M32 10l-8 7"/></svg>
  </div>
  <div class="oct-num" style="left:447px;color:#111">2</div>
  <div class="oct" style="left:780px;background:var(--light);color:#222">
    <h3>Investment Marketing</h3>
    <p>Lorem ipsum dolor sit amet consectetur adipiscing elit, sed do eiusmod tempor incididunt ut labore et dolore</p>
    <svg style="margin-top:20px" width="34" height="20" fill="none" stroke="#111" stroke-width="2"><path d="M2 10h30M32 10l-8-7M32 10l-8 7"/></svg>
  </div>
  <div class="oct-num" style="left:780px;color:#111">3</div>

  <h2 class="section-title" style="top:2906px;color:#111">Our Projects</h2>
  <div class="ph" style="left:111px;top:3005px;width:309px;height:516px;background:linear-gradient(180deg,#0d1a2a 0%,#34404c 45%,#0b0e12 100%)" role="img" aria-label="Photo of a dark high-rise tower">
    <svg class="abs" style="left:130px;top:240px" width="48" height="48" fill="none" stroke="#e8b830" stroke-width="2"><circle cx="20" cy="20" r="17"/><path d="M20 11v18M11 20h18M32 32l12 12"/></svg>
    <div class="proj-overlay">
      <div style="font:700 22px var(--serif)">Project Title Goes Here</div>
      <div style="font:400 15px/24px var(--sans);margin-top:10px">Lorem ipsum dolor sit amet consectetur adipiscing elit, sed do eiusmod tempor.</div>
    </div>
  </div>
  <div class="ph" style="left:447px;top:3005px;width:306px;height:298px;background:linear-gradient(180deg,#eceae6,#cfc8bd 55%,#8b7560)" role="img" aria-label="Photo of a bright living room with a sofa"></div>
  <div class="ph" style="left:447px;top:3332px;width:306px;height:189px;background:linear-gradient(180deg,#8fb0c4,#5e7480 55%,#2c3238)" role="img" aria-label="Photo of a hillside villa at dusk"></div>
  <div class="ph" style="left:780px;top:3005px;width:307px;height:191px;background:linear-gradient(180deg,#f5f5f3,#d9d9d6 60%,#b5a88a)" role="img" aria-label="Photo of a white dining room with stairs"></div>
  <div class="ph" style="left:780px;top:3223px;width:307px;height:298px;background:linear-gradient(170deg,#bcd4ec,#5d88b5 50%,#2d4c6e 80%,#f2f2f2)" role="img" aria-label="Photo of a modern blue glass apartment tower"></div>
  <div class="btn" style="left:512px;top:3575px;width:175px;height:45px">View More</div>

  <section class="abs reasons" role="img" aria-label="Grayscale photo of business people in a meeting"></section>
  <h2 class="section-title" style="top:3846px;color:#fff">Plenty Of Reasons To Choose Us</h2>

  <div class="hex" style="left:136px">
    <svg class="shape" width="286" height="467"><polygon points="143,0 286,150 286,317 143,467 0,317 0,150" fill="#f2c53d"/></svg>
    <svg class="abs" style="left:108px;top:120px" width="70" height="70" fill="none" stroke="#fff" stroke-width="4"><path d="M8 64h56M16 62V38M28 62V30M40 62V22M52 62V34M6 14h14M6 22h14M6 30h14M52 4l3 6 6 1-4 4 1 6-6-3-6 3 1-6-4-4 6-1z"/></svg>
    <div class="in"><h3>Excellent Reputation</h3><p>Lorem ipsum dolor sit amet consectetur adipiscing elit, sed do eiusmod tempor incididunt ut labore et dolore</p></div>
  </div>
  <div class="hex" style="left:457px">
    <svg class="shape" width="286" height="467"><polygon points="143,0 286,150 286,317 143,467 0,317 0,150" fill="#fff"/></svg>
    <svg class="abs" style="left:108px;top:120px" width="70" height="70" fill="none" stroke="#c9a22c" stroke-width="4"><path d="M6 34L35 8l29 26M14 28v34h42V28"/><circle cx="35" cy="36" r="7"/><path d="M24 62c0-12 22-12 22 0"/></svg>
    <div class="in"><h3>Best Local Agents</h3><p>Lorem ipsum dolor sit amet consectetur adipiscing elit, sed do eiusmod tempor incididunt ut labore et dolore</p></div>
  </div>
  <div class="hex" style="left:778px">
    <svg class="shape" width="286" height="467"><polygon points="143,0 286,150 286,317 143,467 0,317 0,150" fill="#fff"/></svg>
    <svg class="abs" style="left:108px;top:120px" width="70" height="70" fill="none" stroke="#c9a22c" stroke-width="4"><rect x="20" y="4" width="30" height="30"/><path d="M26 12h18M26 20h18M26 28h18M4 64h62M10 64V40h50v24M22 64v-12h10v12M38 64v-12h10v12"/></svg>
    <div class="in"><h3>Quick Service</h3><p>Lorem ipsum dolor sit amet consectetur adipiscing elit, sed do eiusmod tempor incididunt ut labore et dolore</p></div>
  </div>

  <section class="abs map" role="img" aria-label="Street map of the office neighbourhood"></section>
  <svg class="abs" style="left:586px;top:4640px" width="30" height="40" viewBox="0 0 24 32"><path d="M12 0C5 0 0 5 0 12c0 9 12 20 12 20s12-11 12-20C24 5 19 0 12 0z" fill="#111"/><circle cx="12" cy="12" r="4.5" fill="#fff"/></svg>
  <div class="abs map-label">214 Harlow Street<br>Kenton</div>

  <footer>
    <div class="abs brand" style="left:111px;top:4890px">
      <div class="brand-mark" style="width:54px;height:54px"></div>
      <div><div class="brand-name" style="color:#111">Brisk Vale</div><div class="brand-sub" style="color:#333">REAL ESTATE</div></div>
    </div>
    <svg class="abs" style="left:111px;top:4968px" width="20" height="20" viewBox="0 0 24 24" fill="none" stroke="#111" stroke-width="1.8"><path d="M5 3h4l2 5-3 2a12 12 0 0 0 6 6l2-3 5 2v4a2 2 0 0 1-2 2A18 18 0 0 1 3 5a2 2 0 0 1 2-2z"/></svg>
    <div class="abs" style="left:144px;top:4966px;font:400 15px/21px var(--sans);color:#222">Call Us:<br>555-318-2046</div>
    <svg class="abs" style="left:111px;top:5034px" width="22" height="16" fill="none" stroke="#111" stroke-width="1.8"><rect x="1" y="1" width="20" height="14"/><path d="M1 1l10 8 10-8"/></svg>
    <div class="abs" style="left:144px;top:5030px;font:400 15px/21px var(--sans);color:#222">Email Us:<br>hello@brisk-vale.com</div>
    <div class="social" style="left:112px" aria-label="Social link"></div>
    <div class="social" style="left:169px;background:#111" aria-label="Social link"></div>
    <div class="social" style="left:225px;background:#111" aria-label="Social link"></div>

    <div class="foot-h" style="left:418px;top:4878px">Quick Links</div>
    <div class="abs foot-links" style="left:418px;top:4922px">
      <a>Home</a><a>About Us</a><a>Projects</a><a>Blog</a><a>Contact</a>
    </div>

    <div class="foot-h" style="left:601px;top:4878px">Get In Touch</div>
    <div class="field" style="left:601px;top:4927px;width:237px;height:43px">Enter Your Name</div>
    <div class="field" style="left:854px;top:4927px;width:233px;height:43px">Email Address</div>
    <div class="field" style="left:601px;top:4981px;width:486px;height:109px">Message</div>
    <div class="btn" style="left:601px;top:5104px;width:486px;height:43px">Submit Now</div>

    <div class="abs copy">COPYRIGHT © 2021 <b style="font-weight:600;color:#111">BRISK VALE</b>. ALL RIGHTS RESERVED.</div>
  </footer>
</div>
</body>
</html>
```